Bex2Court Sign

Sign will be used to advertise my personal injury law firm. Sign will be 4' x 8'. With that in mind, I want it to pop, but not too busy. I have two logos I use, so feel free to incorporate either of those. I have attached a couple photos of me to choose from, the two logos (use one if it fits), and I want the sign to say something to the effect of "Car Accident?" Call me. Ask for Bex. 866-BEX2CRT." I have also attached a sign design that I had made on another project. Feel free to use for inspiration.
Updates

I appreciate all the designs, but pretty much every one looks the same. I was hoping for some variety. It looks like most of the designers are using the same template. I know the sign is small, so it doesn't allow for much. But I have updated my "brief" and included some examples of signs that stood out to me. Hope this helps.

Requirements
Must have
• Car Accident?
Call me. Ask for Bex.
866-BEX2CRT
Veteran Owned
Photo of me
Nice to have
• My Bex2Court logo

```html
<!DOCTYPE html>
<html lang="en">
<head>
<meta charset="utf-8">
<title>Bex2Court Sign</title>
<link rel="stylesheet" href="https://fonts.googleapis.com/css2?family=Poppins:wght@300;400;600;800;900&display=swap">
<style>
  :root {
    --backdrop: #b3b3b3;
    --sign-white: #ffffff;
    --sign-grey: #e6e6e6;
    --ink: #0b0b0b;
    --forest: #2c5225;
    --bright-green: #2f8a3a;
    --teal: #1d5a73;
    --divider: #8c8c8c;
    --photo-light: #d8d1c8;
    --photo-dark: #3e4b36;
  }
  html, body {
    margin: 0;
    padding: 0;
    width: 789px;
    height: 1200px;
    overflow: hidden;
    background: var(--backdrop);
  }
  .canvas {
    position: relative;
    width: 789px;
    height: 1200px;
  }
  .sign {
    position: absolute;
    left: 50px;
    top: 427px;
    width: 688px;
    height: 345px;
    box-shadow: 8px 10px 14px rgba(0, 0, 0, 0.45);
  }
  .sign svg {
    display: block;
    width: 100%;
    height: 100%;
  }
  .headline {
    font-family: "Poppins", sans-serif;
    font-weight: 900;
    fill: var(--ink);
  }
  .call-strong {
    font-family: "Poppins", sans-serif;
    font-weight: 800;
    fill: var(--sign-white);
  }
  .call-light {
    font-family: "Poppins", sans-serif;
    font-weight: 300;
    fill: var(--sign-white);
  }
  .phone {
    font-family: "Poppins", sans-serif;
    font-weight: 800;
    fill: var(--sign-white);
  }
  .firm-name {
    font-family: "Poppins", sans-serif;
    font-weight: 600;
    fill: var(--forest);
  }
  .veteran-label {
    font-family: "Poppins", sans-serif;
    font-weight: 400;
    fill: var(--teal);
  }
</style>
</head>
<body>
<main class="canvas">
  <section class="sign" aria-label="Bex2Court road sign">
    <svg viewBox="0 0 1365 685" xmlns="http://www.w3.org/2000/svg">
      <defs>
        <linearGradient id="sign-face" x1="0" y1="0" x2="0" y2="1">
          <stop offset="0" stop-color="var(--sign-grey)"/>
          <stop offset="0.35" stop-color="var(--sign-white)"/>
          <stop offset="1" stop-color="var(--sign-white)"/>
        </linearGradient>
        <linearGradient id="portrait-tones" x1="0" y1="0" x2="0" y2="1">
          <stop offset="0" stop-color="var(--photo-light)"/>
          <stop offset="0.45" stop-color="#b9a793"/>
          <stop offset="1" stop-color="var(--photo-dark)"/>
        </linearGradient>
      </defs>

      <rect class="sign-face" width="1365" height="685" fill="url(#sign-face)"/>

      <text class="headline" x="40" y="140" font-size="118" textLength="1005" lengthAdjust="spacingAndGlyphs">CAR ACCIDENT?</text>

      <g class="call-band">
        <polygon points="0,180 912,180 852,268 0,268" fill="var(--teal)"/>
        <polygon points="912,180 928,180 868,268 852,268" fill="var(--bright-green)"/>
        <text x="40" y="253" font-size="78">
          <tspan class="call-strong">CALL ME</tspan><tspan class="call-light">. Ask for Bex.</tspan>
        </text>
      </g>

      <g class="phone-band">
        <rect x="0" y="290" width="1090" height="148" fill="var(--forest)"/>
        <text class="phone" x="40" y="407" font-size="122" textLength="865" lengthAdjust="spacingAndGlyphs">866-BEX2CRT</text>
      </g>

      <g class="firm-lockup">
        <text class="firm-name" x="40" y="572" font-size="68" textLength="385" lengthAdjust="spacingAndGlyphs">Bex2Court</text>
        <line x1="483" y1="508" x2="483" y2="606" stroke="var(--divider)" stroke-width="2"/>
        <rect class="veteran-badge" x="550" y="500" width="165" height="82" fill="var(--teal)"/>
        <text class="veteran-label" x="632" y="616" font-size="21" text-anchor="middle" textLength="158" lengthAdjust="spacingAndGlyphs">VETERAN OWNED</text>
      </g>

      <g class="base-stripes">
        <polygon points="0,645 180,645 220,685 0,685" fill="var(--forest)"/>
        <polygon points="208,648 860,648 860,685 230,685" fill="var(--teal)"/>
      </g>

      <g class="attorney-portrait" role="img" aria-label="Portrait photo of the attorney in a green blazer and white shirt">
        <path d="M1040,80 Q1050,15 1150,15 Q1245,15 1250,90 L1255,300 Q1260,360 1365,400 L1365,685 L845,685 L850,470 Q870,400 1040,330 Z" fill="url(#portrait-tones)"/>
      </g>
    </svg>
  </section>
</main>
</body>
</html>
```